Varlowe Supply Partners
Business Cards and Stationary
Project: Varlowe Supply Partners
Varlowe Supply Partners -
Creative Brief
Professional
Daniel Varlowe
Manufacturer's Representative
20375 82nd Lane NW Elk Ridge, MN 55492
dvarlowe@varlowesupply-example.com
www.varlowesupply-example.com

```html
<!DOCTYPE html>
<html lang="en">
<head>
<meta charset="utf-8">
<title>Varlowe Supply Partners – Business Cards</title>
<link rel="stylesheet" href="https://fonts.googleapis.com/css2?family=Cinzel:wght@500&family=Open+Sans:wght@400;600&display=swap">
<style>
  :root {
    --backdrop: #e9e7e3;
    --card: #ffffff;
    --brand-blue: #1f5fae;
    --brand-deep: #0f3f86;
    --brand-light: #5d95d6;
    --swoosh-grey: #c4c8cf;
    --ink: #2b2b2b;
    --ink-soft: #6b6f76;
    --on-blue: #ffffff;
  }
  * { box-sizing: border-box; margin: 0; padding: 0; }
  html, body { width: 1200px; height: 758px; overflow: hidden; }
  body { background: var(--backdrop); font-family: "Open Sans", Arial, sans-serif; position: relative; }

  .card {
    position: absolute; width: 555px; height: 330px;
    background: var(--card); overflow: hidden;
    box-shadow: 0 6px 16px rgba(0,0,0,.18);
  }
  .card--front { left: 45px; top: 70px; }
  .card--alt   { left: 620px; top: 70px; }
  .card--back  { left: 322px; top: 420px; }

  .card__swoosh { position: absolute; inset: 0; width: 100%; height: 100%; }

  .brand { position: absolute; display: flex; align-items: center; gap: 14px; color: var(--brand-blue); font-family: "Cinzel", Georgia, serif; font-weight: 500; }
  .brand__dot { border-radius: 50%; background: var(--brand-blue); flex: none; }
  .brand__name { line-height: 1.05; }
  .brand__name span { display: block; }
  .brand__name .lead { font-size: 44px; letter-spacing: 1px; }
  .brand__name .trail { font-size: 21px; letter-spacing: 1.5px; }

  .card--front .brand { left: 34px; top: 44px; }
  .card--front .brand__dot { width: 74px; height: 74px; }
  .card--alt .brand { left: 40px; top: 100px; }
  .card--alt .brand__dot { width: 70px; height: 70px; }

  .person { position: absolute; left: 34px; top: 198px; display: flex; align-items: baseline; gap: 28px; }
  .person__name { font-size: 16px; color: var(--ink); }
  .person__role { font-size: 11px; color: var(--ink-soft); }

  .contact { position: absolute; left: 34px; top: 236px; display: grid; grid-template-columns: auto auto; column-gap: 22px; row-gap: 5px; font-size: 9.5px; color: var(--ink-soft); }
  .contact__item { display: flex; align-items: center; gap: 6px; }
  .contact__item--wide { grid-column: 1 / 3; }
  .icon { width: 11px; height: 11px; flex: none; }

  .address { position: absolute; right: 40px; top: 250px; font-size: 10px; color: var(--on-blue); line-height: 1.45; }

  .corner-dot { position: absolute; right: 34px; bottom: 30px; width: 34px; height: 34px; border-radius: 50%; background: rgba(255,255,255,.28); }

  .card--back .back-mark { position: absolute; left: 38px; top: 62px; width: 170px; height: 170px; border-radius: 50%; background: var(--brand-blue); }
  .card--back .web { position: absolute; right: 84px; bottom: 36px; font-size: 10px; color: var(--on-blue); }
</style>
</head>
<body>

<svg width="0" height="0" style="position:absolute">
  <defs>
    <linearGradient id="swooshBlue" x1="0" y1="1" x2="1" y2="0">
      <stop offset="0" stop-color="var(--brand-light)"/>
      <stop offset=".55" stop-color="var(--brand-blue)"/>
      <stop offset="1" stop-color="var(--brand-deep)"/>
    </linearGradient>
  </defs>
</svg>

<!-- Front -->
<section class="card card--front">
  <svg class="card__swoosh" viewBox="0 0 555 330" preserveAspectRatio="none" aria-hidden="true">
    <path d="M0,330 L0,318 C200,306 420,240 555,92 L555,330 Z" fill="var(--swoosh-grey)"/>
    <path d="M0,330 L0,326 C210,318 430,250 555,112 L555,330 Z" fill="url(#swooshBlue)"/>
  </svg>
  <div class="brand">
    <div class="brand__dot"></div>
    <div class="brand__name"><span class="lead">VARLOWE</span><span class="trail">SUPPLY PARTNERS</span></div>
  </div>
  <div class="person">
    <span class="person__name">Daniel Varlowe</span>
    <span class="person__role">Manufacturer's Representative</span>
  </div>
  <div class="contact">
    <div class="contact__item">
      <svg class="icon" viewBox="0 0 12 12"><path d="M3 1l2 2-1 1.5c.7 1.5 2 2.8 3.5 3.5L9 7l2 2-1.5 2C5 10.5 1.5 7 1 2.5Z" fill="var(--ink-soft)"/></svg>612.555.0148
    </div>
    <div class="contact__item">
      <svg class="icon" viewBox="0 0 12 12"><rect x="1" y="3" width="10" height="6" rx="1" fill="none" stroke="var(--ink-soft)"/><path d="M3 3V1h6v2M3 9v2h6V9" fill="none" stroke="var(--ink-soft)"/></svg>612.555.0193
    </div>
    <div class="contact__item contact__item--wide">
      <svg class="icon" viewBox="0 0 12 12"><rect x="1" y="2.5" width="10" height="7" fill="none" stroke="var(--ink-soft)"/><path d="M1 2.5l5 4 5-4" fill="none" stroke="var(--ink-soft)"/></svg>dvarlowe@varlowesupply-example.com
    </div>
    <div class="contact__item contact__item--wide">
      <svg class="icon" viewBox="0 0 12 12"><circle cx="6" cy="6" r="5" fill="none" stroke="var(--ink-soft)"/><path d="M1 6h10M6 1c-2.5 3-2.5 7 0 10M6 1c2.5 3 2.5 7 0 10" fill="none" stroke="var(--ink-soft)"/></svg>www.varlowesupply-example.com
    </div>
  </div>
  <p class="address">20375 82nd Lane NW<br>Elk Ridge, MN 55492</p>
</section>

<!-- Alternate front -->
<section class="card card--alt">
  <svg class="card__swoosh" viewBox="0 0 555 330" preserveAspectRatio="none" aria-hidden="true">
    <path d="M0,330 L0,318 C200,306 420,240 555,92 L555,330 Z" fill="var(--swoosh-grey)"/>
    <path d="M0,330 L0,326 C210,318 430,250 555,112 L555,330 Z" fill="url(#swooshBlue)"/>
  </svg>
  <div class="brand">
    <div class="brand__dot"></div>
    <div class="brand__name"><span class="lead">VARLOWE</span><span class="trail">SUPPLY PARTNERS</span></div>
  </div>
  <div class="corner-dot"></div>
</section>

<!-- Back -->
<section class="card card--back">
  <svg class="card__swoosh" viewBox="0 0 555 330" preserveAspectRatio="none" aria-hidden="true">
    <path d="M0,330 L0,318 C200,306 420,240 555,92 L555,330 Z" fill="var(--swoosh-grey)"/>
    <path d="M0,330 L0,326 C210,318 430,250 555,112 L555,330 Z" fill="url(#swooshBlue)"/>
  </svg>
  <div class="back-mark"></div>
  <div class="corner-dot"></div>
  <p class="web">www.varlowesupply-example.com</p>
</section>

</body>
</html>
```